Swimming Pool Service business card needed!!!! Please

Hi Everyone! Thanks for looking at my contest. I PROMISE to provide excellent feedback during this process.

I am starting a new swimming pool cleaning business in San Diego, California and would like your help in making a business card for me.

I like easy to read, classy and sophisticated.

I am having a website designed and I'm looking for it to have pictures of really clean & clear pools.

I really like the blue on white color format, but open to other colors.

I do not have a logo, but the name of my company is GLIMMERTIDE POOL SERVICE.

My tag line is: Pools so clean, you can see yourself "in" them. (does not need to have the quotes around "in"...maybe just italics for this word IN?) You decide for me.

I would like to have a logo designed that incorporates some sort of easy to read letters. I do not want cursive (handwriting) letters. I thought about having a "reflection" of letters (mirror image), but think that this will be hard to read from far away. Maybe you can surprise me and come up with an idea that works using the a mirror image....but I'm not sure. I was leaning toward plain old BLOCK letters as I think it would be easy to read on my truck.

I would like to have the NAQTR and WBK logos on the back of the card. I have attached those two as files. You can put other things on the back as well, but I need these two logos on there. Or maybe put them on the front of the card if you have a better idea for the back of the card! :-)

Maybe blue on the back of the card and white on the front of the card? I don't know, I'm just thinking out loud.

I had another card done awhile ago called HARBORLINE TEES. I have uploaded a copy of that card for your reference. I don't want this card to be the same as my new company is a swimming pool cleaning company, but I wanted you to see what I liked in the past.

THANK YOU!!!!
Updates

Reason: Partner out of town and want their feedback....so need more time to decide and designs still coming in.

Industry/Entity Type

Business

Contact Information for Business Card

GLIMMERTIDE POOL SERVICE
Dale Wexby
Owner
4817 Quarry Bend Ave. #512
San Diego, CA 92417
858-291-6083
www.glimmertidepoolservice.example

Font styles to use
Sans Serif

Colors
0255a3
3176b5
ffffff

Requirements
Nice to have
• Some things to (possibly) add to back of card (in no particular order)
• WBK logo
• NAQTR logo
• Free Estimates
• Residential and Commercial Services
• Equipment Repairs
• Saltwater Systems
• Licensed, Bonded, Insured
• Family Owned and Operated
• No Contracts
• =======================
• Check out the FolioMint business card that i attached.
• i think they did this using a chrome overlay.
• Can any of you guys design that? or is that done at my printer?
• ==================
Should not have
• Hi Designers-
• The first round of cards came back and let's stay away from the light blue (powder blue) color. I don't like the look of it on the business cards.
• Also, the pool company JPG's that I attached are other logos of pool companies that I liked. I don't want them to be on my card. The only logos that should be on my card are the one you are going to come up with for my company, the WBK logo and the NAQTR logo.
• Lastly, no vertical cards and no split cards (logo on left, contact info on right side).
• Thanks much!

```html
<!DOCTYPE html>
<html lang="en">
<head>
<meta charset="utf-8">
<title>Glimmertide Pool Service – Business Card</title>
<link rel="stylesheet" href="https://fonts.googleapis.com/css2?family=Roboto:ital,wght@0,400;0,700;1,400&family=Roboto+Condensed:wght@700&display=swap">
<style>
  :root {
    --brand-blue: #0255a3;
    --mid-blue: #3176b5;
    --water-light: #5fb2e6;
    --water-deep: #1f86cf;
    --paper: #ffffff;
    --backdrop: #eef0f2;
    --ink: #1d4f8f;
  }
  * { box-sizing: border-box; margin: 0; padding: 0; }
  html, body {
    width: 1200px; height: 478px; overflow: hidden;
    background: var(--backdrop);
  }
  .sheet {
    width: 1200px; height: 478px;
    display: flex; align-items: center; justify-content: center; gap: 30px;
  }
  .card {
    position: relative;
    width: 560px; height: 305px;
    background: var(--paper);
    overflow: hidden;
    box-shadow: 0 2px 6px rgba(0,0,0,.15);
  }
  .card svg.art { position: absolute; inset: 0; width: 100%; height: 100%; }

  .tagline {
    position: absolute; left: 50px; top: 38px;
    font-family: "Roboto", sans-serif; font-weight: 400;
    font-size: 15px; color: var(--paper); letter-spacing: .2px;
  }
  .company-name {
    position: absolute; right: 34px; bottom: 22px;
    font-family: "Roboto Condensed", sans-serif; font-weight: 700;
    font-size: 33px; line-height: 1; text-align: right;
    color: var(--brand-blue); letter-spacing: .5px;
  }

  .contact {
    position: absolute; left: 28px; top: 32px;
    font-family: "Roboto", sans-serif; font-weight: 400;
    font-size: 18px; line-height: 1.3; color: var(--ink);
  }
  .contact .owner { margin-bottom: 4px; }
  .badges {
    position: absolute; right: 34px; bottom: 34px;
    display: flex; gap: 16px;
  }
  .badge {
    width: 60px; height: 60px; border-radius: 50%;
    background: var(--paper);
    border: 3px solid var(--mid-blue);
  }
  .badge.alt { border-color: #c9342f; }
</style>
</head>
<body>
<main class="sheet">

  <section class="card card-front">
    <svg class="art" viewBox="0 0 560 305" preserveAspectRatio="none">
      <defs>
        <linearGradient id="water" x1="0" y1="0" x2="1" y2="1">
          <stop offset="0" stop-color="var(--water-light)"/>
          <stop offset="1" stop-color="var(--water-deep)"/>
        </linearGradient>
      </defs>
      <rect width="560" height="305" fill="url(#water)" role="img" aria-label="Rippling clear pool water"/>
      <path d="M0,205 C120,170 230,165 330,190 C420,212 490,205 560,185 L560,305 L0,305 Z" fill="var(--paper)"/>
      <path d="M0,198 C120,162 230,156 330,182 C420,204 490,198 560,176" fill="none" stroke="#bfe1f5" stroke-width="5" opacity=".8"/>
    </svg>
    <p class="tagline">Pools so clean you can see yourself</p>
    <h1 class="company-name">GLIMMERTIDE<br>POOL SERVICE</h1>
  </section>

  <section class="card card-back">
    <svg class="art" viewBox="0 0 560 305" preserveAspectRatio="none">
      <path d="M0,222 C150,175 330,160 560,190 L560,205 C330,180 170,195 0,250 Z" fill="var(--brand-blue)"/>
      <path d="M0,258 C170,203 330,190 560,213" fill="none" stroke="var(--mid-blue)" stroke-width="3"/>
    </svg>
    <address class="contact">
      <p class="owner">Dale Wexby Owner</p>
      <p>4817 Quarry Bend Ave.</p>
      <p>#512 San Diego,</p>
      <p>CA 92417 858-291-6083</p>
    </address>
    <div class="badges">
      <span class="badge" aria-label="WBK certification badge"></span>
      <span class="badge alt" aria-label="NAQTR membership badge"></span>
    </div>
  </section>

</main>
</body>
</html>
```